Product Description page for Hullwrap.com, References here just need a clean up redesign

Hi, were working on updating the product description page of our site hullwrap.com

Attached is a reference of what we drew on paint. We want to keep it pretty much the same as far as whats on there, the components with a few small adjustments and a clean actually designed look.

1. We want to remove the tabs (product description, warranty, reviews) and put it all in that main content area stretching down into sections. IE: Product Description section, followed by reviews, followed by warranty, below each other.
2. The side bar needs to be redesigned as far as the look and feel but the content and whats in there should stay the same.
3. The main banner area will be replaced shortly you do not have to worry about that.
4. Include a section or box for people to put in their email for a free Ebook.

Target Market(s)

people looking to easily view our boat cover products and buy without having to click too often or leave the page.

Industry/Entity Type

Online Shopping

Number of Pages Required

1 page

Requirements
Must have
• - Must update the sidebar
• - Must update the content area to remove the tabs and put the content from each tab sectioned off below each other (dummy text is fine for now for the tabs you cant view)
Nice to have
• - Cool place thats clean and functional to insert a section for people to put in their email to receive a free ebook
Should not have
• - too much change, we already know what we want and have a solid reference to work from.

```html
<!DOCTYPE html>
<html lang="en">
<head>
<meta charset="utf-8">
<title>Hullwrap.com – Center Console with Bow Rails</title>
<link href="https://fonts.googleapis.com/css2?family=Lato:wght@400;700;900&family=Roboto+Condensed:wght@400;700&display=swap" rel="stylesheet">
<style>
:root{
  --brand:#1f5fb4;
  --brand-dark:#173f86;
  --ink:#222;
  --text:#444;
  --muted:#777;
  --line:#ddd;
  --accent:#e8552c;
  --accent-deep:#d24a22;
  --star:#f3a521;
  --dark:#2f2f2f;
  --green:#7cc243;
  --navy:#0f2e8c;
  --page:#f4f4f4;
}
*{box-sizing:border-box;margin:0;padding:0}
html,body{width:684px;height:1200px;overflow:hidden}
body{position:relative;background:#fff;font-family:"Lato",sans-serif;color:var(--text)}
.abs{position:absolute}
svg.defs{position:absolute;width:0;height:0}
.stars{display:inline-flex;gap:2px;vertical-align:middle}
.stars svg{width:9px;height:9px}

/* header */
.header{left:0;top:0;width:684px;height:42px;background:linear-gradient(#fff,#f4f4f4)}
.logo{left:78px;top:10px;display:flex;align-items:center;gap:6px;font-weight:900;font-size:21px;color:var(--brand);letter-spacing:-.3px}
.logo-dot{width:16px;height:16px;border-radius:50%;background:var(--brand)}
.phone{left:490px;top:8px;text-align:right;width:118px}
.phone-num{font-family:"Roboto Condensed",sans-serif;font-weight:700;font-size:15px;color:#2348c9;display:flex;align-items:center;justify-content:flex-end;gap:5px}
.phone-num svg{width:14px;height:11px}
.phone-hours{font-size:6.5px;color:#666;margin-top:1px}
.nav{left:0;top:43px;width:684px;height:20px;background:linear-gradient(#fafafa,#e9e9e9);border-top:1px solid #ddd;border-bottom:1px solid #ccc}
.nav-list{position:absolute;left:72px;top:0;display:flex;height:19px;align-items:center;font-size:8.5px;color:#333;list-style:none}
.nav-list li{padding:0 12px;border-right:1px solid #ccc;line-height:12px}
.nav-list li:last-child{border-right:none}
.checkout{left:501px;top:44px;width:107px;height:17px;background:linear-gradient(#3b83dc,#1f5fb4);border-radius:2px;color:#fff;font-family:"Roboto Condensed",sans-serif;font-size:7.5px;font-weight:700;display:flex;align-items:center;justify-content:center;gap:4px}
.checkout svg{width:10px;height:9px}
.crumbs{left:0;top:66px;width:684px;height:26px;background:var(--dark);color:#fff;font-size:7.5px;font-weight:700}
.crumbs ol{list-style:none;display:flex;gap:8px;position:absolute;left:74px;top:9px}
.crumbs li+li::before{content:"›";margin-right:8px}

/* main card */
.card{left:75px;top:92px;width:533px;height:822px;background:#fff;box-shadow:0 0 8px rgba(0,0,0,.15)}
.hero{left:84px;top:106px;width:316px;height:167px;border:1px solid #ccc;background:#fff}
.hero-fill{position:absolute;left:6px;top:20px;width:302px;height:124px;border-radius:40px 60px 8px 8px;background:linear-gradient(#24467a 0%,#31558e 45%,#dfe4ea 60%,#c7ccd2 100%)}
.thumbs{left:84px;top:278px;width:316px;height:52px;background:#eee;border:1px solid #e2e2e2}
.thumbs-inner{position:absolute;left:14px;top:0;width:288px;height:50px;background:#fff;display:flex;gap:8px;padding:5px 18px}
.thumb{width:45px;height:42px;border:1px solid #ccc}
.thumbs .arr{position:absolute;top:18px;font-size:9px;color:#bbb}
.section-title{font-size:9.5px;font-weight:700;color:var(--ink)}
.desc{left:98px;top:345px;width:290px}
.desc p{font-size:7.4px;line-height:12px;margin-top:6px;color:#333}
.features{left:98px;top:432px;width:290px}
.features ul{list-style:none;margin-top:8px}
.features li{font-size:7px;color:#333;line-height:12px;position:relative;padding-left:11px;margin-bottom:11.4px}
.features li::before{content:"";position:absolute;left:2px;top:5px;width:3px;height:3px;border-radius:50%;background:#333}
.avg{left:98px;top:724px;display:flex;align-items:center;gap:6px}
.avg .val{font-size:9px;font-weight:700;color:var(--ink)}
.review{left:98px;width:290px}
.review .head{display:flex;align-items:center;gap:10px;font-size:7px;font-weight:700;color:#222}
.review .head .stars svg{width:10px;height:10px}
.review .by{font-size:6.8px;color:#444;margin-top:6px}
.review .by b{font-weight:700}
.review p{font-size:6.8px;line-height:11px;margin-top:5px;color:#444}
.more{left:98px;top:886px;padding:3px 6px;border:1px solid #ddd;background:#f3f3f3;font-size:6.5px;color:#444}

/* buy box */
.title{left:412px;top:106px;width:180px;font-size:13.5px;font-weight:700;color:var(--ink);line-height:16px}
.rating-top{left:413px;top:146px;display:flex;align-items:center;gap:5px;font-size:9px;color:#e89220}
.rating-top .stars svg{width:10px;height:10px}
.old{left:414px;top:166px;font-size:9px;color:#777;text-decoration:line-through}
.sale{left:414px;top:185px;font-size:8.5px;font-weight:700;color:#222}
.sale span{color:var(--accent);font-weight:400}
.price{left:413px;top:203px;font-size:15px;font-weight:700;color:var(--accent)}
.field{left:414px;font-size:7px;font-weight:700;color:#222;display:flex;align-items:center}
.select{border:1px solid #ccc;height:13px;font-size:6.5px;font-weight:400;display:flex;align-items:center;justify-content:space-between;padding:0 4px;position:absolute;background:#fff}
.select::after{content:"";border:3px solid transparent;border-top-color:#888;margin-top:3px}
.swatch{position:absolute;top:231px;width:12px;height:12px;border-radius:50%}
.extras{left:414px;top:277px;width:178px;list-style:none}
.extras li{display:flex;align-items:center;font-size:7px;color:#555;height:14.6px}
.extras .box{width:7px;height:7px;border:1px solid #bbb;margin-right:9px;background:#f7f7f7}
.extras .cost{margin-left:auto;color:var(--accent);font-weight:700}
.cart{left:412px;top:341px;width:180px;height:25px;background:linear-gradient(var(--accent),var(--accent-deep));color:#fff;font-size:9.5px;font-weight:700;display:flex;align-items:center;justify-content:center;letter-spacing:.2px}
.ship{left:412px;top:373px;width:180px;display:flex;justify-content:center;align-items:center;gap:5px;font-size:6.5px;font-style:italic;font-weight:700;color:#3a7a2e}
.ship svg{width:15px;height:9px}
.also{left:407px;top:401px;width:187px;height:24px;background:var(--dark);color:#fff;font-size:10px;font-weight:700;display:flex;align-items:center;justify-content:center}
.pcard{left:407px;width:187px;height:223px;border:1px solid #e2e2e2;box-shadow:0 0 3px rgba(0,0,0,.06);background:#fff}
.pcard .shot{position:absolute;left:14px;top:10px;width:159px;height:110px;border-radius:4px}
.pcard .name{position:absolute;left:0;width:185px;text-align:center;font-size:7.6px;font-weight:700;color:#111}
.pcard .buy{position:absolute;left:0;width:185px;height:20px;background:var(--accent-deep);color:#fff;font-size:8px;font-weight:700;display:flex;align-items:center;justify-content:center}
.pcard .line{position:absolute;left:8px;font-size:7.6px;color:#444;display:flex;align-items:center;gap:6px}
.pcard .free{color:var(--accent);font-weight:700}

/* newsletter */
.nl-title{left:73px;top:950px;font-size:17px;font-weight:700;color:#1d6fb0}
.nl-text{left:75px;top:976px;width:230px;font-size:7.8px;line-height:11px;color:#222}
.nl-form{left:321px;top:970px;width:287px;height:33px;border:1px solid #ddd;border-radius:17px;background:#fff}
.nl-form .ph{position:absolute;left:12px;top:11px;font-size:8.5px;font-style:italic;color:#888}
.nl-form .go{position:absolute;right:2px;top:2px;width:96px;height:27px;border-radius:14px;background:linear-gradient(#8fce55,#6db23a);color:#fff;font-weight:700;font-size:10px;display:flex;align-items:center;justify-content:center}

/* footer */
.scene{left:0;top:1025px;width:684px;height:175px;background:linear-gradient(#fff 0%,#c9d6e2 14%,#8aa0b6 30%,#51697e 42%,#3d5a3e 48%,#2a5c9a 56%,#2a58ad 75%,#1b3f9a 100%)}
.foot-bar{left:75px;top:1126px;width:533px;height:22px;background:linear-gradient(#1d4fb7,#123a94);border-radius:3px;color:#fff;font-size:6.8px;font-weight:700}
.foot-bar .lead{position:absolute;left:13px;top:7px}
.foot-bar .in{position:absolute;left:144px;top:4px;width:103px;height:13px;background:#fff;border-radius:1px}
.foot-bar .sub{position:absolute;left:247px;top:4px;width:45px;height:13px;background:#f26a1b;font-size:6px;display:flex;align-items:center;justify-content:center}
.foot-bar .links{position:absolute;right:10px;top:7px;display:flex;gap:6px;text-decoration:underline}
.copy{left:0;top:1166px;width:684px;text-align:center;font-size:5.8px;line-height:8px;color:#7f8fbf}
.copy u{color:#c9d2ee}
</style>
</head>
<body>
<svg class="defs" aria-hidden="true">
  <defs>
    <linearGradient id="half"><stop offset="50%" stop-color="#f3a521"/><stop offset="50%" stop-color="#d8d8d8"/></linearGradient>
    <symbol id="star" viewBox="0 0 20 20"><path d="M10 1l2.7 6 6.3.6-4.8 4.3 1.4 6.4L10 15l-5.6 3.3 1.4-6.4L1 7.6 7.3 7z"/></symbol>
  </defs>
</svg>

<header class="abs header">
  <div class="abs logo"><span class="logo-dot"></span>HULLWRAP.com</div>
  <div class="abs phone">
    <div class="phone-num"><svg viewBox="0 0 14 11"><path d="M1 3c0-2 12-2 12 0v1h-3V3H4v1H1z M3 5h8l2 5H1z" fill="#2348c9"/></svg>(800) 555-0147</div>
    <div class="phone-hours">Store Hours(M-F, 9:30AM - 6PM PST)</div>
  </div>
</header>
<nav class="abs nav">
  <ul class="nav-list">
    <li>Boat Covers</li><li>Bass Boat Covers</li><li>T Top Boat Covers</li><li>Bimini Tops</li><li>Jet Ski Covers</li>
  </ul>
</nav>
<div class="abs checkout"><svg viewBox="0 0 10 9"><path d="M0 1h2l1.5 5h5L10 2H3" fill="none" stroke="#fff" stroke-width="1.2"/><circle cx="4" cy="8" r="1" fill="#fff"/><circle cx="8" cy="8" r="1" fill="#fff"/></svg>CHECKOUT : (0) Items ▾</div>
<div class="abs crumbs"><ol><li>Home</li><li>Boat Covers</li><li>Runabout w</li><li>up to 16'8" Long and 90" Wide</li></ol></div>

<main>
<div class="abs card"></div>
<div class="abs hero"><div class="hero-fill" role="img" aria-label="Blue cover fitted over a runabout boat on a trailer"></div></div>
<div class="abs thumbs">
  <span class="arr" style="left:4px">‹</span>
  <div class="thumbs-inner">
    <div class="thumb" role="img" aria-label="Warranty badge" style="background:linear-gradient(#c23a2a,#555)"></div>
    <div class="thumb" role="img" aria-label="Fabric coating detail" style="background:linear-gradient(#2d5fa8,#7ea2cf)"></div>
    <div class="thumb" role="img" aria-label="Cover strap detail" style="background:linear-gradient(#ddd,#555)"></div>
    <div class="thumb" role="img" aria-label="Buckle close-up" style="background:linear-gradient(#c9c9c9,#333)"></div>
    <div class="thumb" role="img" aria-label="Included tie-down straps" style="background:linear-gradient(#eee,#444)"></div>
  </div>
  <span class="arr" style="right:4px">›</span>
</div>

<section class="abs desc">
  <h2 class="section-title">Description:</h2>
  <p>When a pontoon is stored outside it is exposed to harmful elements such as wind, dirt, rain, and UV. The Tideguard Supreme is the most powerful cover available providing 10x more strength and protection compared to the competition. The 1200 denier fabric is 100% waterproof and provides excellent protection against sun, rain, wind and snow.</p>
</section>
<section class="abs features">
  <h2 class="section-title">Features:</h2>
  <ul>
    <li>5 Star Fit. Fit guaranteed or your money back</li>
    <li>10 Year Warranty. Full warranty covering rips and tears</li>
    <li>The covers comes in Grey, Blue and Maroon</li>
    <li>The fabric is pure 100% Marine Polyester (no cotton mix)</li>
    <li>No worries, the cover won't stretch or shrink</li>
    <li>Rain or sleet the cover is 100% waterproof</li>
    <li>Fully Breathable, you'll never see mold or mildew</li>
    <li>UV resistant and also prevents heat buildup</li>
    <li>Fully Trailerable (straps included)</li>
    <li>The cover also comes with an integrated hem cord to be used when mooring or on boat lifts</li>
    <li>Tough - Strong - Durable</li>
  </ul>
</section>

<div class="abs avg"><h2 class="section-title">Average Customer Rating:</h2>
  <span class="stars"><svg fill="#f3a521"><use href="#star"/></svg><svg fill="#f3a521"><use href="#star"/></svg><svg fill="#f3a521"><use href="#star"/></svg><svg fill="#f3a521"><use href="#star"/></svg><svg fill="url(#half)"><use href="#star"/></svg></span>
  <span class="val">(4.8)</span></div>
<article class="abs review" style="top:744px">
  <div class="head"><span class="stars"><svg fill="#f3a521"><use href="#star"/></svg><svg fill="#f3a521"><use href="#star"/></svg><svg fill="#f3a521"><use href="#star"/></svg><svg fill="#f3a521"><use href="#star"/></svg><svg fill="#f3a521"><use href="#star"/></svg></span>Great boat cover</div>
  <div class="by">Reviewed by <b>Sam K</b> (SAINT PETERSBURG, FL) — Feb 22, 2016 5:34 PM</div>
  <p>Lorem ipsum dolor sit amet, consectetuer adipiscing elit, sed diam nonummy euismod tincidunt ut laoreet dolore magna aliqua</p>
</article>
<article class="abs review" style="top:813px">
  <div class="head"><span class="stars"><svg fill="#f3a521"><use href="#star"/></svg><svg fill="#f3a521"><use href="#star"/></svg><svg fill="#f3a521"><use href="#star"/></svg><svg fill="#f3a521"><use href="#star"/></svg><svg fill="#f3a521"><use href="#star"/></svg></span>Great boat cover</div>
  <div class="by">Reviewed by <b>Sam K</b> (SAINT PETERSBURG, FL) — Feb 22, 2016 5:34 PM</div>
  <p>Lorem ipsum dolor sit amet, consectetuer adipiscing elit, sed diam nonummy euismod tincidunt ut laoreet dolore magna aliqua</p>
</article>
<div class="abs more">Load More</div>

<aside>
  <h1 class="abs title">Center Console with Bow Rails</h1>
  <div class="abs rating-top"><span class="stars"><svg fill="#f3a521"><use href="#star"/></svg><svg fill="#f3a521"><use href="#star"/></svg><svg fill="#f3a521"><use href="#star"/></svg><svg fill="#f3a521"><use href="#star"/></svg><svg fill="url(#half)"><use href="#star"/></svg></span>(1,607)</div>
  <div class="abs old">$ 442.00</div>
  <div class="abs sale">On Sale: <span>10% Off</span></div>
  <div class="abs price">$ 331.50</div>
  <div class="abs field" style="top:233px">Color*:</div>
  <div class="select" style="left:455px;top:230px;width:95px">SELECT</div>
  <span class="swatch" style="left:556px;background:#1d7cc7"></span>
  <span class="swatch" style="left:573px;background:#777"></span>
  <div class="abs field" style="top:256px">Quantity*:</div>
  <div class="select" style="left:455px;top:253px;width:33px">1</div>
  <ul class="abs extras">
    <li><span class="box"></span>Guaranteed Rush Production<span class="cost">$25.00</span></li>
    <li><span class="box"></span>Harborline Boat Cover Storage<span class="cost">$11.69</span></li>
    <li><span class="box"></span>Harborline Lock and Cable<span class="cost">$18.99</span></li>
    <li><span class="box"></span>Harborline Gust Guard<span class="cost">$11.69</span></li>
  </ul>
  <div class="abs cart">ADD TO CART</div>
  <div class="abs ship"><svg viewBox="0 0 15 9"><rect x="0" y="1" width="9" height="6" fill="#3a7a2e"/><path d="M9 3h3l2 2v2H9z" fill="#3a7a2e"/><circle cx="3" cy="8" r="1.2" fill="#3a7a2e"/><circle cx="11.5" cy="8" r="1.2" fill="#3a7a2e"/></svg>Free Shipping!</div>
  <div class="abs also">You may also like</div>

  <div class="abs pcard" style="top:442px">
    <div class="shot" role="img" aria-label="Black and blue cover on a jet ski trailer" style="background:linear-gradient(#fff 10%,#2d5fc4 35%,#222 55%,#bbb 80%,#fff)"></div>
    <div class="name" style="top:130px">1 Seater Jet Ski Cover Fits up to 100"</div>
    <div class="buy" style="top:144px">BUY NOW</div>
    <div class="line" style="top:170px">From $152.10</div>
    <div class="line free" style="top:186px">Free Shipping</div>
    <div class="line" style="top:202px">Rating <span class="stars"><svg fill="#f3a521"><use href="#star"/></svg><svg fill="#f3a521"><use href="#star"/></svg><svg fill="#f3a521"><use href="#star"/></svg><svg fill="#f3a521"><use href="#star"/></svg><svg fill="url(#half)"><use href="#star"/></svg></span>(1k+)</div>
  </div>
  <div class="abs pcard" style="top:677px">
    <div class="shot" role="img" aria-label="Blue bimini top on a metal frame" style="background:linear-gradient(#fff 5%,#2c3f9e 25%,#e8eaf0 45%,#fff)"></div>
    <div class="name" style="top:131px">Bimini Tops</div>
    <div class="buy" style="top:147px">BUY NOW</div>
    <div class="line" style="top:172px">From $350.10</div>
    <div class="line free" style="top:188px">Free Shipping</div>
    <div class="line" style="top:202px">Rating <span class="stars"><svg fill="#f3a521"><use href="#star"/></svg><svg fill="#f3a521"><use href="#star"/></svg><svg fill="#f3a521"><use href="#star"/></svg><svg fill="#f3a521"><use href="#star"/></svg><svg fill="url(#half)"><use href="#star"/></svg></span>(1k+)</div>
  </div>
</aside>
</main>

<section>
  <h2 class="abs nl-title">Subscribe to our Newsletter</h2>
  <p class="abs nl-text">Lorem ipsum dolor sit amet, ex vim quem primis. Quot suav molestiae ex usu. Ridens eleifend ei sea.</p>
  <div class="abs nl-form"><span class="ph">Enter Your Email</span><span class="go">Sign Up</span></div>
</section>

<footer>
  <div class="abs scene" role="img" aria-label="Harbor with moored sailboats before misty mountains"></div>
  <div class="abs foot-bar">
    <span class="lead">Sign Up To Win A FREE Boat Cover!</span>
    <span class="in"></span><span class="sub">Subscribe ›</span>
    <span class="links"><span>Exchanges &amp; Returns</span><span>Contact Us</span></span>
  </div>
  <div class="abs copy">Copyright © 2016. hullwrap.com. All Rights Reserved<br>120 Marina Bend Road, Port Alder NY 10990<br><u>Privacy Policy</u></div>
</footer>
</body>
</html>
```